Monthly Mailed Newsletter/Magazine for Medical Spa

Every month we send out a mailed newsletter/magazine to our visitors from the previous month. We made a sample newsletter/magazine as a guideline of what we are looking for. We need a designer to make a simple and clean design layout.

- Attached is our sample design that has all the content we want to use.
- Newsletter/magazine is 8 pages total.
- Size of each page is 8.5 inches in width by 11 inches in height.
- Content and images can be located here: https://files.vornacloud.net/shared/8kqTRw3ZpLmX2vNcA7yHd5EbJ0sUgFo4e?view=open

The following will give you an idea of our brand presentation.
Our website is: www.GlowDermaClinic.com
Our Instagram; @glowdermaclinic
Our Facebook: www.socialtreo.com/glowdermaclinic

Target Market(s)

Women 25 - 45

Industry/Entity Type

Beauty

Font styles to use
Other font styles liked:
• Josefins Sans Bold & Lato

Colors
f78f20
ffffff

Requirements
Must have
• - Our Logo
- Our tagline: YOUR SKIN DESERVES IT!
- Address and contact information for our locations
- Our color scheme: Black and #FAA641
- Heading font is Josefin Sans Bold
- Paragraph font is Lato
- Our website address: www.GlowDermaClinic.com

```html
<!DOCTYPE html>
<html lang="en">
<head>
<meta charset="UTF-8">
<title>Is At-Home Laser Hair Removal Effective?</title>
<link href="https://fonts.googleapis.com/css2?family=Josefin+Sans:ital,wght@0,300;0,400;0,700;1,300;1,700&family=Lato:wght@400;700&display=swap" rel="stylesheet">
<style>
  :root {
    --orange: #f7941d;
    --orange-soft: #fab27a;
    --orange-light: #fcd2ae;
    --cream: #efe9df;
    --leaf: #2f6b3a;
    --ink: #111111;
    --white: #ffffff;
  }
  * { margin: 0; padding: 0; box-sizing: border-box; }
  html, body {
    width: 927px;
    height: 1200px;
    overflow: hidden;
    background: var(--white);
  }
  .page {
    position: relative;
    width: 927px;
    height: 1200px;
    overflow: hidden;
    background: linear-gradient(to bottom,
      var(--white) 0%,
      var(--white) 42%,
      #fde3cc 55%,
      var(--orange-soft) 68%,
      var(--orange) 85%,
      var(--orange) 100%);
  }
  .hero-photo {
    position: absolute;
    left: 0;
    top: 0;
    width: 452px;
    height: 427px;
    background:
      radial-gradient(ellipse at 12% 40%, var(--leaf) 0%, rgba(47,107,58,0.6) 25%, rgba(47,107,58,0) 48%),
      linear-gradient(135deg, #f3eee6 0%, var(--cream) 60%, #e6ddcf 100%);
  }
  .title-panel {
    position: absolute;
    left: 467px;
    top: 0;
    width: 460px;
    height: 427px;
    background: var(--orange);
    padding: 44px 0 0 58px;
    color: var(--white);
  }
  .kicker {
    font-family: "Josefin Sans", sans-serif;
    font-weight: 300;
    font-style: italic;
    font-size: 29px;
    letter-spacing: 1.5px;
    color: var(--ink);
    margin-bottom: 22px;
  }
  .headline {
    font-family: "Josefin Sans", sans-serif;
    font-weight: 700;
    font-size: 57px;
    line-height: 64px;
    letter-spacing: 2px;
    text-transform: uppercase;
  }
  .pull-quote {
    position: absolute;
    left: 27px;
    top: 440px;
    font-family: "Josefin Sans", sans-serif;
    font-weight: 400;
    font-size: 33px;
    color: var(--orange-light);
    white-space: nowrap;
  }
  .article {
    position: absolute;
    left: 27px;
    top: 506px;
    width: 887px;
    font-family: "Lato", sans-serif;
    font-size: 19.5px;
    line-height: 26.6px;
    color: var(--ink);
  }
  .portrait-photo {
    float: right;
    width: 373px;
    height: 373px;
    margin: -18px 0 8px 20px;
    background: linear-gradient(160deg, #f4f2ee 0%, #e9e4dc 45%, #d8c2ad 100%);
  }
  .intro { width: 490px; }
  .faq-question {
    font-family: "Lato", sans-serif;
    font-weight: 700;
    font-style: italic;
    color: var(--white);
    margin-top: 2px;
  }
  .faq-answer { color: var(--white); }
</style>
</head>
<body>
  <main class="page">
    <div class="hero-photo" role="img" aria-label="Photo of a woman's smooth legs in mustard heeled mules beside tropical leaves on a cream background"></div>

    <header class="title-panel">
      <p class="kicker">THE UNBIASED TRUTH</p>
      <h1 class="headline">Is At-Home<br>Laser Hair<br>Removal<br>Effective?</h1>
    </header>

    <p class="pull-quote">'I love how prickly your skin feels'said no one ever!</p>

    <article class="article">
      <div class="portrait-photo" role="img" aria-label="Photo of a smiling woman in a white towel using an at-home laser device on her underarm"></div>
      <p class="intro">Did you know that the average modern woman shaves 7,718 times in one lifetime? That's a whole lot of bristling, ingrown hairs, and skin irritation. Thankfully laser treatments have rendered razors obsolete. If you're already a firm laser believer, the marketability of handy at-home DIY products can be appealing. But many are left perplexed at their effectiveness. Here are some unbiased professional opinions to zap away your FAQs.</p>

      <h2 class="faq-question">How does laser hair removal work?</h2>
      <p class="faq-answer">Laser hair removal uses a concentrated beam of light to target melanin, also known as your natural pigment. Through this, the follicle that produces hair is damaged. This delays the future growth of hairs.</p>

      <h2 class="faq-question">Do at-home laser hair removal gadgets work?</h2>
      <p class="faq-answer">NYC's dermatology professionals answer the million-dollar question with a very cautionary yes. Dr. Arun Malhotra claims that results vary according to individuals. Success is dependant on the contrast between your hair and skin color. Light skin and dark hair produce the best outcomes, while other combinations can prove them ineffective. Generally, at-home products are more suitable for use on smaller areas such as your lip and underarms. They can also be beneficial for maintenance after in-office treatments.</p>
    </article>
  </main>
</body>
</html>
```